New Company Business Card design

Looking for a corporate looking business card utilising my new logo design - the logo i would like embossed as one option and flat as another - simplistic but stylish - less is more - we are an import export business launching into the market - i would like a couple of options as main background - Grey or Black

```html
<!DOCTYPE html>
<html lang="en">
<head>
<meta charset="utf-8">
<title>Meridian Trade Partners – Business Card</title>
<link href="https://fonts.googleapis.com/css2?family=Lato:wght@400;700&display=swap" rel="stylesheet">
<style>
  :root {
    --stage: #e6e6e6;
    --card-dark: #2b2b2d;
    --mark-dark: #3a3a3d;
    --card-light: #ffffff;
    --brand-blue: #1e6fbf;
    --brand-grey: #8a8a8d;
    --text-dark: #3d3d3f;
    --divider: #d4d4d4;
  }
  * { margin: 0; padding: 0; box-sizing: border-box; }
  html, body { width: 1200px; height: 862px; overflow: hidden; }
  body {
    background: var(--stage);
    font-family: "Lato", Arial, sans-serif;
    position: relative;
  }
  .card {
    position: absolute;
    width: 540px;
    height: 308px;
    overflow: hidden;
  }
  .card-front {
    left: 70px; top: 90px;
    background: var(--card-dark);
    border-bottom: 8px solid var(--brand-blue);
  }
  .card-back {
    left: 590px; top: 464px;
    background: var(--card-light);
  }
  .brand {
    position: absolute;
    display: flex;
    align-items: center;
    gap: 12px;
    font-weight: 700;
    font-size: 26px;
    letter-spacing: 1px;
    text-transform: uppercase;
    line-height: 1.1;
  }
  .brand-dot { width: 18px; height: 18px; border-radius: 50%; flex: none; }
  .card-front .brand { left: 0; right: 0; top: 118px; justify-content: center; color: var(--mark-dark); }
  .card-front .brand-dot { background: var(--mark-dark); }
  .card-back .brand { left: 36px; top: 118px; width: 250px; font-size: 21px; color: var(--brand-blue); }
  .card-back .brand-dot { background: var(--brand-blue); }
  .divider {
    position: absolute; left: 300px; top: 60px;
    width: 1px; height: 160px; background: var(--divider);
  }
  .contact { position: absolute; left: 322px; top: 64px; color: var(--text-dark); font-size: 14px; line-height: 1.45; }
  .contact-name { color: var(--brand-blue); font-weight: 700; font-size: 19px; line-height: 1.2; }
  .contact-title { margin-bottom: 10px; }
  .contact-address { margin-bottom: 8px; }
  .contact-row { display: flex; align-items: center; gap: 8px; }
  .contact-row svg { width: 13px; height: 13px; flex: none; }
  .band-grey { position: absolute; left: 0; right: 0; bottom: 12px; height: 6px; background: var(--brand-grey); }
  .band-blue { position: absolute; left: 0; right: 0; bottom: 0; height: 12px; background: var(--brand-blue); }
</style>
</head>
<body>
  <section class="card card-front">
    <div class="brand"><span class="brand-dot"></span>Meridian Trade Partners</div>
  </section>

  <section class="card card-back">
    <div class="brand"><span class="brand-dot"></span><span>Meridian Trade Partners</span></div>
    <div class="divider"></div>
    <div class="contact">
      <div class="contact-name">Samuel Whitford</div>
      <div class="contact-title">Teaching Pastor</div>
      <div class="contact-address">418 N Harbor Lane<br>Carlton, MS 39100</div>
      <div class="contact-row">
        <svg viewBox="0 0 16 16" aria-hidden="true"><path d="M4 1l3 3-2 2c1 2 3 4 5 5l2-2 3 3-2 2C7 14 2 9 2 3z" fill="var(--brand-blue)"/></svg>
        <span>000.000.0000</span>
      </div>
      <div class="contact-row">
        <svg viewBox="0 0 16 16" aria-hidden="true"><rect x="1.5" y="3.5" width="13" height="9" fill="none" stroke="var(--brand-blue)" stroke-width="1.4"/><path d="M1.5 3.5l6.5 5 6.5-5" fill="none" stroke="var(--brand-blue)" stroke-width="1.4"/></svg>
        <span>samuel@yourwebsite.com</span>
      </div>
      <div class="contact-row">
        <svg viewBox="0 0 16 16" aria-hidden="true"><circle cx="8" cy="8" r="6.5" fill="none" stroke="var(--brand-blue)" stroke-width="1.4"/><path d="M1.5 8h13M8 1.5c-3 3.5-3 9.5 0 13M8 1.5c3 3.5 3 9.5 0 13" fill="none" stroke="var(--brand-blue)" stroke-width="1.2"/></svg>
        <span>www.yourwebsite.com</span>
      </div>
    </div>
    <div class="band-grey"></div>
    <div class="band-blue"></div>
  </section>
</body>
</html>
```